HIgh-end jewelry designer needs a business card design

I need a business card design for the ecclectic & rather expensive jewelry designs. My approach to my work is to combine very old jewelry offset with contemporary items. I enjoy the idea of legacy as well as repurposing finely crafted items that are not possible to create any longer. My desire is to celebrate the past in a contemporary & funky way. The name of my business is VELLORINE. I see my business card design as simple & yet enigmatic as possible. In the end... clean, simple & understated is the look I am after. Thank you for your consideration...

Target Market(s)

I will use this business card for the trade as well as customers

Industry/Entity Type

Business

Contact Information for Business Card

Marta Quorrin Owner/Designer 555-203-7718

Requirements
Must have
• Clean & simple sophisticated design using the word "Vellorinne" as the logo. I like the idea of a play on the word itself, perhaps even using different fonts (i.e.: a bold helvetica combined with a lovely script). I'm afraid to say more because I don't want to limit creative input. Gosh, sometimes it's ok to break the rules!
Nice to have
• In my mind, I have imagined this business card to be simple, using my company name "Vellorine" in a playful yet sophisticated manner. I believe that doing something beautifully simple can be a true challenge. I have imagined something with just black & white, however I am open to ideas... after all that's why I'm here!
Should not have
• As Mozart once said... "It has too many notes!" I know I'm being silly, but I don't want it to be complicated or overly ornate.

```html
<!DOCTYPE html>
<html lang="en">
<head>
<meta charset="utf-8">
<title>Vellorinne — Business Card</title>
<link rel="stylesheet" href="https://fonts.googleapis.com/css2?family=Josefin+Sans:wght@200;400&family=Oswald:wght@300;500&display=swap">
<style>
  :root {
    --backdrop: #e4e2de;
    --card-black: #141414;
    --card-black-edge: #262626;
    --silver-light: #f2f2f2;
    --silver-mid: #cfcfcf;
    --silver-dark: #9a9a9a;
    --stitch: #6d6d6d;
    --ink-dark: #4a4a4a;
    --ink-soft: #707070;
    --name-white: #ffffff;
  }
  html, body {
    margin: 0;
    width: 1200px;
    height: 902px;
    overflow: hidden;
    background: var(--backdrop);
  }
  .canvas {
    position: relative;
    width: 1200px;
    height: 902px;
  }
  .card {
    position: absolute;
    left: 100px;
    top: 165px;
    width: 1000px;
    height: 572px;
    border-radius: 6px;
    overflow: hidden;
    background: var(--card-black);
    box-shadow: 0 18px 40px rgba(0,0,0,0.25);
  }
  .card-shapes {
    position: absolute;
    inset: 0;
  }
  .wordmark {
    position: absolute;
    left: 150px;
    top: 300px;
    margin: 0;
    font-family: "Josefin Sans", sans-serif;
    font-weight: 200;
    font-size: 112px;
    letter-spacing: 2px;
    color: var(--ink-dark);
    line-height: 1;
  }
  .owner {
    position: absolute;
    right: 70px;
    top: 70px;
    text-align: right;
  }
  .owner-name {
    margin: 0;
    font-family: "Oswald", sans-serif;
    font-weight: 500;
    font-size: 52px;
    color: var(--name-white);
    line-height: 1.05;
  }
  .owner-role {
    margin: 4px 0 0;
    font-family: "Oswald", sans-serif;
    font-weight: 300;
    font-size: 22px;
    color: var(--name-white);
  }
  .contact {
    position: absolute;
    left: 150px;
    top: 460px;
    margin: 0;
    padding: 0;
    list-style: none;
    font-family: "Josefin Sans", sans-serif;
    font-weight: 400;
    font-size: 22px;
    color: var(--ink-soft);
  }
  .contact li {
    display: flex;
    align-items: center;
    gap: 14px;
    margin-bottom: 12px;
  }
  .contact-icon {
    width: 16px;
    height: 16px;
    flex: none;
  }
</style>
</head>
<body>
<main class="canvas">
  <section class="card" aria-label="Vellorinne business card">
    <svg class="card-shapes" width="1000" height="572" viewBox="0 0 1000 572" aria-hidden="true">
      <defs>
        <linearGradient id="silverFinish" x1="0" y1="0" x2="1" y2="1">
          <stop offset="0" stop-color="var(--silver-dark)"/>
          <stop offset="0.45" stop-color="var(--silver-light)"/>
          <stop offset="0.75" stop-color="var(--silver-mid)"/>
          <stop offset="1" stop-color="var(--silver-dark)"/>
        </linearGradient>
      </defs>
      <path class="silver-panel" fill="url(#silverFinish)"
        d="M0,250 L150,250 C190,250 200,230 215,200 C260,110 340,70 430,70 C560,70 640,160 660,280 C668,320 690,340 740,340 L1000,340 L1000,572 L0,572 Z"/>
      <path class="stitch-line" fill="none" stroke="var(--stitch)" stroke-width="1.5" stroke-dasharray="4 4"
        d="M0,242 L150,242 C185,242 194,224 208,196 C254,102 336,62 430,62 C566,62 648,154 668,278 C675,316 696,332 740,332 L1000,332"/>
    </svg>

    <h1 class="wordmark">Vellorinne</h1>

    <div class="owner">
      <p class="owner-name">Marta Quorrin</p>
      <p class="owner-role">Owner / Designer</p>
    </div>

    <ul class="contact">
      <li>
        <svg class="contact-icon" viewBox="0 0 16 16" aria-hidden="true"><rect x="1" y="1" width="14" height="14" rx="2" fill="none" stroke="var(--ink-soft)" stroke-width="2"/></svg>
        555-203-7718
      </li>
      <li>
        <svg class="contact-icon" viewBox="0 0 16 16" aria-hidden="true"><rect x="1" y="1" width="14" height="14" rx="2" fill="var(--ink-soft)"/></svg>
        mquorrin@inbox.com
      </li>
    </ul>
  </section>
</main>
</body>
</html>
```